Book cover needed for a major new book on emotional resilience

The book will be titled: 'Storm to Stillness: from rigid habits to pioneers of renewal - The handbook for building steady teams and institutions'
My websites are http://www.brightmarrow.com and http://www.hollenquay.org and I am http://en.pedialoom.org/wiki/Tomas_Brenhurst_(uncertainty_scholar) ad expert in developing emotional resilience. My previous book was The Quiet Compass.
The premise of the book is to introduce brand new material which is the first ever methodology and strategy on how to develop emotional resilience across entire populations like organisations and companies or moving people from fear about change to finding flow through resilience.
The final design should communicate the fact that this is a strategy and methodology. That it is about developing people and entire organisations to be more resilient and who are able to deal with change better.
Target Market(s)
Consultants, Organisational development consultants, Human Resource professionals.

```html
<!DOCTYPE html>
<html lang="en">
<head>
<meta charset="utf-8">
<title>Storm to Stillness — Tomas Brenhurst</title>
<link href="https://fonts.googleapis.com/css2?family=Arimo:wght@400&family=Work+Sans:ital,wght@0,200;1,200&display=swap" rel="stylesheet">
<style>
  :root {
    --sea-deep: #123f45;
    --sea-mid: #2f6266;
    --sea-light: #6f9a97;
    --sea-foam: #a9c6c0;
    --ink-light: #ffffff;
  }
  html, body {
    margin: 0;
    padding: 0;
    width: 750px;
    height: 1200px;
    overflow: hidden;
    background: var(--sea-deep);
  }
  .cover {
    position: relative;
    width: 750px;
    height: 1200px;
    overflow: hidden;
    color: var(--ink-light);
  }
  .cover__sea {
    position: absolute;
    inset: 0;
    background:
      radial-gradient(ellipse 90% 18% at 60% 28%, rgba(111,154,151,0.45), transparent 70%),
      radial-gradient(ellipse 80% 14% at 30% 55%, rgba(169,198,192,0.35), transparent 70%),
      radial-gradient(ellipse 90% 16% at 55% 70%, rgba(169,198,192,0.35), transparent 70%),
      radial-gradient(ellipse 70% 12% at 20% 80%, rgba(111,154,151,0.4), transparent 70%),
      linear-gradient(180deg, var(--sea-mid) 0%, var(--sea-deep) 22%, var(--sea-mid) 48%, var(--sea-light) 62%, var(--sea-mid) 78%, var(--sea-deep) 100%);
  }
  .cover__author {
    position: absolute;
    top: 143px;
    left: 0;
    right: 0;
    text-align: center;
    font-family: "Arimo", "Helvetica Neue", Arial, sans-serif;
    font-weight: 400;
    font-size: 31px;
    letter-spacing: 0.2px;
  }
  .cover__title {
    position: absolute;
    top: 345px;
    left: 0;
    right: 0;
    margin: 0;
    text-align: center;
    font-family: "Work Sans", "Helvetica Neue", sans-serif;
    font-weight: 200;
    text-transform: uppercase;
    line-height: 1;
  }
  .cover__title-line {
    display: block;
  }
  .cover__title-line--first {
    font-size: 172px;
    letter-spacing: 14px;
    margin-right: -14px;
    height: 168px;
  }
  .cover__title-line--joiner {
    font-size: 172px;
    letter-spacing: 14px;
    margin-right: -14px;
    height: 160px;
  }
  .cover__title-line--last {
    font-style: italic;
    font-size: 104px;
    letter-spacing: 6px;
    margin-right: -6px;
    margin-top: 18px;
  }
  .cover__subtitle {
    position: absolute;
    top: 1000px;
    left: 0;
    right: 0;
    margin: 0;
    text-align: center;
    font-family: "Arimo", "Helvetica Neue", Arial, sans-serif;
    font-weight: 400;
    font-size: 24px;
    line-height: 34.5px;
  }
</style>
</head>
<body>
  <main class="cover">
    <div class="cover__sea" role="img" aria-label="Photograph of dark teal ocean waves with pale streaks of foam"></div>
    <p class="cover__author">Tomas Brenhurst</p>
    <h1 class="cover__title">
      <span class="cover__title-line cover__title-line--first">Storm</span>
      <span class="cover__title-line cover__title-line--joiner">To</span>
      <span class="cover__title-line cover__title-line--last">Stillness</span>
    </h1>
    <p class="cover__subtitle">
      From rigid habits to<br>
      pioneers of renewal<br>
      The handbook for building steady<br>
      teams and institutions
    </p>
  </main>
</body>
</html>
```